Start-up Cleaning Business Needs Professional Business Cards

Marta's Butler Cleaning, LLC, is a start-up business based in the Northern Virginia suburbs of Washington, DC. MBC provides cleaning and housekeeping services for homes and offices. We have three core values:

1. We are personal. We value knowing and being known by our customers and each other. If you want nameless, faceless service, you should choose another provider. We put "personal" at the front of the list, because it is most important to us; the design we choose will convey this value.

2. Like a hotel concierge, we are professional in attitude, posture, communication and processes.

3. Like a hotel concierge, we solve problems with a can-do attitude and never make excuses.

Our uniforms are khaki pants with pink polo shirts.

Our logo is attached. There are other symbols, not represented in our logo, that may convey our values well, such as a top hat and bow tie, magnifying glass, desk bell, etc.

Please include fields for an individual's name and title, office phone number, mobile phone number, email address and website address (www.martasbutlercleaning.example).

Standard U.S. size: 2" x 3.5"
Updates

I should have mentioned that the purpose of all our advertising - business cards included - is to motivate potential customers to call or email to arrange a free in-home estimate.

```html
<!DOCTYPE html>
<html lang="en">
<head>
<meta charset="utf-8">
<title>Marta's Butler Cleaning – Business Card</title>
<link rel="stylesheet" href="https://fonts.googleapis.com/css2?family=Exo+2:wght@300;400;600&display=swap">
<style>
  :root {
    --backdrop: #e9e7e3;
    --card-white: #ffffff;
    --card-grey-light: #f7f7f7;
    --card-grey-dark: #dcdcdc;
    --accent-pink: #ee4a9c;
    --ink-logo: #4a4a4a;
    --ink-text: #4a2f36;
    --card-shadow: rgba(0,0,0,0.18);
  }
  * { margin: 0; padding: 0; box-sizing: border-box; }
  html, body {
    width: 1200px; height: 903px; overflow: hidden;
    background: var(--backdrop);
    font-family: "Exo 2", sans-serif;
  }
  .canvas { position: relative; width: 1200px; height: 903px; }

  .card {
    position: absolute;
    width: 600px; height: 343px;
    box-shadow: 0 6px 18px var(--card-shadow);
    overflow: hidden;
  }
  .card--front {
    left: 300px; top: 70px;
    background: var(--card-white);
    display: flex; align-items: center; justify-content: center;
  }
  .card--back {
    left: 300px; top: 490px;
    background: radial-gradient(ellipse at 35% 35%, var(--card-grey-light), var(--card-grey-dark));
  }

  .brand-name {
    font-weight: 300;
    color: var(--ink-logo);
    letter-spacing: 1px;
    line-height: 1;
  }
  .card--front .brand-name { font-size: 92px; }
  .card--back .brand-name {
    position: absolute; left: 92px; top: 14px; font-size: 54px;
  }

  .accent-block {
    position: absolute; left: 0; top: 26px;
    width: 76px; height: 22px;
    background: var(--accent-pink);
  }
  .accent-bar {
    position: absolute; left: 330px; right: 0; top: 148px;
    height: 26px;
    background: var(--accent-pink);
  }

  .address {
    position: absolute; left: 38px; top: 148px;
    display: flex; gap: 8px;
    font-size: 12px; line-height: 17px; color: var(--ink-text);
  }
  .address svg { flex: none; margin-top: 1px; }

  .person { position: absolute; left: 340px; top: 182px; color: var(--ink-text); }
  .person__name { font-size: 16px; font-weight: 600; letter-spacing: 1.5px; }
  .person__title { font-size: 13px; margin-top: 1px; }

  .contacts {
    position: absolute; left: 340px; top: 232px;
    list-style: none;
    font-size: 11px; color: var(--ink-text);
  }
  .contacts li { display: flex; align-items: center; gap: 7px; height: 18px; }
  .contacts svg { flex: none; }
</style>
</head>
<body>
<div class="canvas">

  <section class="card card--front" aria-label="Card front">
    <span class="brand-name">Marta's</span>
  </section>

  <section class="card card--back" aria-label="Card back">
    <div class="accent-block"></div>
    <span class="brand-name">Marta's</span>
    <div class="accent-bar"></div>

    <div class="address">
      <svg width="12" height="15" viewBox="0 0 12 15" aria-hidden="true">
        <path d="M6 0a6 6 0 0 0-6 6c0 4.5 6 9 6 9s6-4.5 6-9a6 6 0 0 0-6-6z" fill="var(--ink-text)"/>
        <circle cx="6" cy="6" r="2.2" fill="var(--card-grey-light)"/>
      </svg>
      <p>210 Elm Court, Suite 4<br>Fairfax Road VA</p>
    </div>

    <div class="person">
      <p class="person__name">DANIEL REYES</p>
      <p class="person__title">Managing Director</p>
    </div>

    <ul class="contacts">
      <li>
        <svg width="11" height="11" viewBox="0 0 24 24" aria-hidden="true"><path d="M6.6 10.8a15 15 0 0 0 6.6 6.6l2.2-2.2c.3-.3.7-.4 1-.2 1.1.4 2.3.6 3.6.6.6 0 1 .4 1 1V20c0 .6-.4 1-1 1A17 17 0 0 1 3 4c0-.6.4-1 1-1h3.5c.6 0 1 .4 1 1 0 1.3.2 2.5.6 3.6.1.3 0 .7-.2 1z" fill="var(--ink-text)"/></svg>
        555 014 2287
      </li>
      <li>
        <svg width="11" height="11" viewBox="0 0 24 24" aria-hidden="true"><rect x="6" y="1" width="12" height="22" rx="2" fill="none" stroke="var(--ink-text)" stroke-width="2.5"/></svg>
        555 014 2288
      </li>
      <li>
        <svg width="11" height="11" viewBox="0 0 24 24" aria-hidden="true"><rect x="2" y="5" width="20" height="14" fill="var(--ink-text)"/><path d="M2 5l10 8 10-8" fill="none" stroke="var(--card-grey-light)" stroke-width="2"/></svg>
        555 014 2289
      </li>
      <li>
        <svg width="11" height="11" viewBox="0 0 24 24" aria-hidden="true"><rect x="2" y="5" width="20" height="14" fill="var(--ink-text)"/><path d="M2 5l10 8 10-8" fill="none" stroke="var(--card-grey-light)" stroke-width="2"/></svg>
        daniel@martasbutler.example
      </li>
      <li>
        <svg width="11" height="11" viewBox="0 0 24 24" aria-hidden="true"><circle cx="12" cy="12" r="10" fill="none" stroke="var(--ink-text)" stroke-width="2"/><path d="M2 12h20M12 2c3 3 3 17 0 20M12 2c-3 3-3 17 0 20" fill="none" stroke="var(--ink-text)" stroke-width="1.6"/></svg>
        www.martasbutlercleaning.example
      </li>
    </ul>
  </section>

</div>
</body>
</html>
```